SPA small billboard design and A frame sign

🎨 Creative Designers! We have an exciting opportunity for you! 🎨

Are you passionate about graphic design and have a knack for creating captivating pieces that convey a powerful message? Then this is your chance to shine!

We're seeking a spectacular design for the entrance sign of the prestigious Veloma Spa, located within the lush Tamaren Resort in Puerto Viejo, Costa Rica. This spa offers a unique experience where visitors can indulge in top-notch treatments and combine them with enjoying the resort's facilities, including a credit for the restaurant. It's the perfect oasis for relaxation and rejuvenation!

Project Details:

Entrance Sign: Size 100x64 cm. We want a captivating design that beckons people to enter and experience the luxury and serenity of the Veloma Spa.
A-Frame Signs: Two A-frame signs, one to promote the spa's services and the other for spa days. Size 60x80 cm each.

More information about the Veloma Spa: Download here: veloma.tamaren-example.com

We're looking for designs that reflect the essence of the Veloma Spa and highlight its connection to nature, relaxation, and wellness!

🌟 Ready to be part of this exciting project? Submit your proposals today! 🌟

[Attachment: Tamaren Resort logo, color palette, and reference photos]

```html
<!DOCTYPE html>
<html lang="en">
<head>
<meta charset="utf-8">
<title>Veloma Spa – Entrance Sign</title>
<link rel="stylesheet" href="https://fonts.googleapis.com/css2?family=Lora:wght@500&display=swap">
<style>
  :root {
    --paper: #ffffff;
    --teal-ink: #2e7f88;
    --mint: #8fd9c8;
    --mint-soft: #c9eee4;
    --teal-drop: #3fb3a5;
    --blush: #f3c9e6;
    --lilac: #e7c3ee;
    --mist: #b9cbd6;
    --lily-line: #5f9ea5;
  }
  html, body {
    margin: 0;
    padding: 0;
    overflow: hidden;
    background: var(--paper);
  }
  .sign {
    position: relative;
    width: 1200px;
    height: 768px;
    overflow: hidden;
    background: var(--paper);
  }
  .sign__decor {
    position: absolute;
    inset: 0;
    width: 1200px;
    height: 768px;
  }
  .sign__brand {
    position: absolute;
    left: 0;
    right: 0;
    top: 285px;
    margin: 0;
    text-align: center;
    font-family: "Lora", Georgia, serif;
    font-weight: 500;
    font-size: 150px;
    line-height: 1;
    letter-spacing: -1px;
    color: var(--teal-ink);
  }
</style>
</head>
<body>
<main class="sign">
  <svg class="sign__decor" viewBox="0 0 1200 768" xmlns="http://www.w3.org/2000/svg">
    <defs>
      <radialGradient id="wash-blush" cx="50%" cy="50%" r="50%">
        <stop offset="0%" stop-color="#ffffff"/>
        <stop offset="100%" stop-color="var(--blush)"/>
      </radialGradient>
      <radialGradient id="wash-lilac" cx="40%" cy="40%" r="60%">
        <stop offset="0%" stop-color="#ffffff"/>
        <stop offset="100%" stop-color="var(--lilac)"/>
      </radialGradient>
      <linearGradient id="wash-mint" x1="0" y1="0" x2="1" y2="0">
        <stop offset="0%" stop-color="var(--mint-soft)"/>
        <stop offset="100%" stop-color="var(--mint)"/>
      </linearGradient>
      <linearGradient id="wash-mist" x1="0" y1="0" x2="1" y2="1">
        <stop offset="0%" stop-color="#ffffff"/>
        <stop offset="100%" stop-color="var(--mist)"/>
      </linearGradient>
      <radialGradient id="drop-teal" cx="40%" cy="40%" r="60%">
        <stop offset="0%" stop-color="var(--mint-soft)"/>
        <stop offset="100%" stop-color="var(--teal-drop)"/>
      </radialGradient>
      <linearGradient id="lily-tone" x1="0" y1="0" x2="1" y2="1">
        <stop offset="0%" stop-color="#e6f3f3"/>
        <stop offset="100%" stop-color="#cfe6e7"/>
      </linearGradient>
    </defs>

    <g class="decor-wash" role="img" aria-label="Soft pink and blue watercolour washes across the top">
      <ellipse cx="370" cy="20" rx="170" ry="120" fill="url(#wash-blush)"/>
      <rect x="540" y="0" width="270" height="130" rx="60" fill="url(#wash-mist)" opacity="0.8"/>
      <ellipse cx="130" cy="140" rx="120" ry="40" fill="url(#wash-lilac)" opacity="0.8"/>
      <rect x="0" y="300" width="40" height="120" rx="18" fill="url(#wash-mint)" opacity="0.6"/>
    </g>

    <g class="decor-drops" role="img" aria-label="Teal and pink watercolour droplets">
      <circle cx="30" cy="90" r="55" fill="url(#drop-teal)"/>
      <circle cx="560" cy="30" r="14" fill="url(#drop-teal)"/>
      <circle cx="595" cy="28" r="18" fill="url(#drop-teal)"/>
      <circle cx="1000" cy="0" r="60" fill="url(#drop-teal)"/>
      <circle cx="1095" cy="370" r="9" fill="#c75ab8"/>
      <circle cx="1105" cy="395" r="6" fill="#c75ab8"/>
    </g>

    <g class="decor-lily-top" role="img" aria-label="Line-drawn lily flowers and leaves, top right corner">
      <path d="M790 0 H1200 V470 C1120 430 1020 330 960 250 C900 170 820 80 790 0 Z" fill="url(#lily-tone)" opacity="0.7"/>
    </g>

    <g class="decor-wash-right" role="img" aria-label="Pink and mint watercolour circle, lower right">
      <rect x="960" y="300" width="90" height="150" rx="40" fill="url(#wash-mint)" opacity="0.7"/>
      <circle cx="1080" cy="560" r="160" fill="url(#wash-lilac)"/>
    </g>

    <g class="decor-lily-bottom" role="img" aria-label="Line-drawn lily flowers and leaves, bottom left corner">
      <path d="M0 500 C120 470 260 520 330 600 C390 670 420 730 430 768 H0 Z" fill="url(#lily-tone)" opacity="0.7"/>
    </g>

    <g class="decor-wash-bottom" role="img" aria-label="Mint watercolour brush strokes along the bottom edge">
      <rect x="520" y="690" width="380" height="60" rx="20" fill="url(#wash-mint)" opacity="0.6"/>
      <rect x="330" y="720" width="150" height="48" rx="20" fill="url(#wash-lilac)" opacity="0.7"/>
      <circle cx="900" cy="768" r="50" fill="url(#wash-mint)" opacity="0.6"/>
    </g>
  </svg>

  <h1 class="sign__brand">Veloma Spa</h1>
</main>
</body>
</html>
```